Pale Harbor Recordings looking for artwork for the next release EP

We are an electronic record label looking for a piece of artwork designed for the next EP release. It needs to follow the same style as previous releases. We need the finished design as saved layers (background. foreground, details) as we use this for creating teaser trailer videos. This is for a digital-only release, it won't actually be printed out for CDs.
Dimensions 3000 x 3000

Target Market(s)

Electronic

Colors

Designer to choose colors to be used in the design.

Requirements
Must have
• See attachments for the style of artwork we are looking for. Needs to be in the same format with the same grainy look. Finished design must be delieved as saved layers (background. foreground, details)
Nice to have
• The artist's name is Velvet Lantern , and the name of the EP is called 'Glass Orbit'

```html
<!DOCTYPE html>
<html lang="en">
<head>
<meta charset="utf-8">
<title>Glass Orbit – Velvet Lantern</title>
<link rel="stylesheet" href="https://fonts.googleapis.com/css2?family=Marcellus+SC&display=swap">
<style>
  :root {
    --space-deep: #0c0f24;
    --space-mid: #1d2450;
    --space-haze: #3b4f86;
    --violet: #8a3fd0;
    --violet-light: #c58cf2;
    --chevron: #0a0c1e;
    --portrait-light: #8c86b4;
    --portrait-dark: #3a3566;
    --type: #c9c2d8;
    --logo: #d6cde6;
  }
  html, body {
    margin: 0;
    padding: 0;
    width: 1200px;
    height: 1200px;
    overflow: hidden;
    background: var(--space-deep);
  }
  .cover {
    position: relative;
    width: 1200px;
    height: 1200px;
    overflow: hidden;
    font-family: "Marcellus SC", serif;
  }
  .cover-art {
    position: absolute;
    inset: 0;
    width: 1200px;
    height: 1200px;
    display: block;
  }
  .release-title {
    position: absolute;
    left: 42px;
    top: 30px;
    margin: 0;
    color: var(--type);
    font-weight: 400;
    font-size: 24px;
    letter-spacing: 0.5px;
    line-height: 1.25;
  }
  .release-title .ep-name {
    display: block;
    padding-bottom: 3px;
    border-bottom: 1px solid var(--type);
  }
  .release-title .artist-name {
    display: block;
    padding-top: 3px;
  }
  .label-mark {
    position: absolute;
    right: 44px;
    bottom: 30px;
    width: 150px;
    display: flex;
    flex-direction: column;
    align-items: center;
    gap: 8px;
  }
  .label-mark .label-dot {
    width: 96px;
    height: 96px;
    border-radius: 50%;
    background: var(--logo);
    opacity: 0.85;
  }
  .label-mark .label-name {
    color: var(--logo);
    font-size: 11px;
    letter-spacing: 1.5px;
    text-align: center;
    line-height: 1.3;
  }
</style>
</head>
<body>
<main class="cover">
  <svg class="cover-art" viewBox="0 0 1200 1200" xmlns="http://www.w3.org/2000/svg">
    <defs>
      <radialGradient id="space-glow" cx="0.45" cy="0.42" r="0.75">
        <stop offset="0" stop-color="var(--space-haze)"/>
        <stop offset="0.5" stop-color="var(--space-mid)"/>
        <stop offset="1" stop-color="var(--space-deep)"/>
      </radialGradient>
      <radialGradient id="portrait-tone" cx="0.5" cy="0.45" r="0.6">
        <stop offset="0" stop-color="var(--portrait-light)"/>
        <stop offset="0.7" stop-color="var(--portrait-dark)"/>
        <stop offset="1" stop-color="var(--portrait-dark)" stop-opacity="0"/>
      </radialGradient>
      <linearGradient id="streak" x1="0" x2="1">
        <stop offset="0" stop-color="var(--violet)" stop-opacity="0"/>
        <stop offset="0.3" stop-color="var(--violet-light)" stop-opacity="0.7"/>
        <stop offset="0.7" stop-color="var(--violet)" stop-opacity="0.6"/>
        <stop offset="1" stop-color="var(--violet)" stop-opacity="0"/>
      </linearGradient>
      <filter id="grain">
        <feTurbulence type="fractalNoise" baseFrequency="0.9" numOctaves="2" seed="4"/>
        <feColorMatrix type="saturate" values="0"/>
        <feComponentTransfer><feFuncA type="linear" slope="0.22"/></feComponentTransfer>
      </filter>
    </defs>

    <g class="background">
      <rect width="1200" height="1200" fill="url(#space-glow)" role="img" aria-label="Starfield nebula in deep blue and violet"/>
    </g>

    <g class="chevrons" fill="var(--chevron)">
      <polygon points="480,0 780,0 320,620 0,620 0,560 300,560" opacity="0.35"/>
      <polygon points="180,200 330,200 620,620 330,620" opacity="0.45"/>
      <polygon points="140,425 350,425 760,1200 520,1200" opacity="0.5"/>
      <polygon points="660,40 860,40 1140,680 940,680" opacity="0.45"/>
      <polygon points="940,680 1140,680 900,1200 700,1200" opacity="0.45"/>
      <polygon points="820,0 1000,0 1200,380 1200,620" opacity="0.3"/>
    </g>

    <g class="foreground">
      <ellipse cx="590" cy="600" rx="290" ry="420" fill="url(#portrait-tone)" role="img" aria-label="Portrait of the artist with branching twig hair and one glowing eye"/>
    </g>

    <g class="light-streaks">
      <rect x="0" y="515" width="1200" height="26" fill="url(#streak)" opacity="0.6"/>
      <rect x="0" y="700" width="1200" height="22" fill="url(#streak)"/>
      <rect x="0" y="748" width="1200" height="12" fill="url(#streak)" opacity="0.7"/>
      <rect x="380" y="470" width="520" height="60" fill="url(#streak)" opacity="0.45"/>
      <rect x="940" y="40" width="220" height="50" fill="url(#streak)" opacity="0.7"/>
      <rect x="0" y="1110" width="240" height="8" fill="url(#streak)" opacity="0.6"/>
    </g>

    <rect class="grain" width="1200" height="1200" filter="url(#grain)"/>
  </svg>

  <h1 class="release-title">
    <span class="ep-name">Glass Orbit</span>
    <span class="artist-name">Velvet Lantern</span>
  </h1>

  <div class="label-mark">
    <span class="label-dot"></span>
    <span class="label-name">PALE HARBOR<br>RECORDINGS</span>
  </div>
</main>
</body>
</html>
```